CyberSecurity Company Website Design

DO NOT CONTACT US OUTSIDE OF PIXELBAZAAR.COM!

A professional 5 page website design for a cyber security and risk management company. We want to portray a serious and professional approach to online security and risk management for businesses. We want the website to be easy to navigate but with a modern style.

The website design pages my partners have reviewed and wish to emulate (without copying, of course ) are:
wrenforge.com, larkhollow.com and brunel.com, Gavromill.com

The attached Zip file contains a very basic outline of the format we are looking for. We want a nice, modern design that reflects cyber security, securing networks, and risk management for business.

Target Market(s)

Large corporations with CyberSecurity Needs

Number of Pages Required

5+ page

Colors
ec1f27
ffffff
0293ce

Requirements
Must have
• The 5 pages we need designed are;
• Home page, Services, About Us, Careers and Contact.

```html
<!DOCTYPE html>
<html lang="en">
<head>
<meta charset="utf-8">
<title>Veltrane CyberTech</title>
<link rel="stylesheet" href="https://fonts.googleapis.com/css2?family=Lato:ital,wght@0,400;0,700;1,700&display=swap">
<style>
:root{
  --navy:#121735;
  --deep:#0d1f45;
  --red:#ec1f27;
  --coral:#ef5350;
  --blue:#0293ce;
  --white:#ffffff;
  --ink:#2b2b2b;
  --grey:#8a8a8a;
  --bar:#a3a3a3;
}
*{margin:0;padding:0;box-sizing:border-box}
html,body{width:1200px;height:3442px;overflow:hidden}
body{font-family:'Lato',sans-serif;color:var(--ink);background:var(--white);position:relative}
section,header,footer{position:absolute;left:0;width:1200px}
.abs{position:absolute}
.center{text-align:center;left:0;width:1200px}

/* header */
.site-header{top:0;height:133px;background:var(--navy)}
.brand{left:103px;top:32px;font-size:56px;color:var(--coral);font-weight:400}
.main-nav{right:150px;top:52px;display:flex;gap:38px;font-size:16px;color:var(--white)}
.main-nav .active{color:var(--coral)}
.social{display:flex;gap:10px}
.social span{width:22px;height:22px;background:var(--blue);display:block}
.header-social{right:90px;top:50px}
.header-social span{width:20px;height:20px;background:#3aa0e0}

/* hero */
.hero{top:133px;height:636px;background:linear-gradient(120deg,#0b2a55 0%,#1d5b8f 40%,#2d4660 70%,#3b3f4d 100%)}
.hero-title{top:512px;font-size:50px;font-weight:700;color:var(--white)}
.arrow{font-size:40px;color:var(--white);font-weight:400}

/* about */
.about{top:769px;height:489px;background:var(--white)}
.about-art{left:690px;top:0;width:510px;height:489px;background:radial-gradient(circle at 75% 70%,#1e88c8 0%,#9fd2ee 35%,#f2f7fb 70%)}
.about h2{left:98px;top:62px;font-size:44px;font-weight:400;color:var(--coral)}
.about h3{left:98px;top:112px;font-size:24px;font-weight:400;color:var(--ink)}
.rule{height:3px;background:var(--navy)}
.about .rule{left:98px;top:152px;width:40px}
.about p{left:98px;width:560px;font-size:13.5px;line-height:1.55;color:#555}
.btn{left:98px;top:373px;width:166px;height:38px;background:var(--coral);color:var(--white);font-size:14px;line-height:38px;text-align:center}

/* services */
.services{top:1258px;height:695px;background:radial-gradient(ellipse at 50% 40%,#1f4b86 0%,#132a5a 55%,#0c1a3c 100%)}
.services h2{top:42px;font-size:38px;font-weight:400;color:var(--coral)}
.services .sub{top:88px;font-size:22px;color:var(--white)}
.services .rule{left:580px;top:124px;width:40px;background:var(--white)}
.card{width:203px;height:201px;background:var(--white);text-align:center;padding-top:38px}
.card svg{width:40px;height:40px}
.card h4{font-size:14.5px;font-weight:700;color:var(--navy);margin-top:6px}
.card .mini{width:40px;height:1px;background:#bbb;margin:10px auto 8px}
.card p{font-size:9.5px;line-height:1.45;color:var(--grey);width:150px;margin:0 auto}

/* team */
.team{top:1953px;height:617px;background:var(--white)}
.team h2{top:68px;font-size:40px;font-weight:400;color:var(--coral)}
.team .sub{top:122px;font-size:26px;font-style:italic;font-weight:700;color:#1b2a7a}
.team .sub2{top:156px;font-size:17px;color:var(--coral)}
.team .rule{left:580px;top:202px;width:40px}
.member{width:260px;text-align:center}
.portrait{width:193px;height:193px;border-radius:50%;margin:0 auto;background:radial-gradient(circle at 50% 40%,#b9a596 0%,#6f6158 55%,#2f2d33 100%)}
.member h4{margin-top:38px;font-size:20px;font-weight:400;color:var(--coral)}
.member .role{font-size:13px;color:var(--navy)}
.member .social{justify-content:center;gap:6px;margin-top:12px}
.member .social span{width:18px;height:18px;background:#1f5fa8}

/* testimonials */
.voices{top:2570px;height:556px;background:linear-gradient(180deg,#e8474a 0%,#e2383d 100%)}
.voices h2{top:60px;font-size:40px;font-weight:400;color:var(--white)}
.voices .sub{top:110px;font-size:23px;color:var(--white)}
.voices .rule{left:580px;top:152px;width:40px;background:var(--white)}
.quote{width:278px;height:184px;background:var(--white);border-radius:6px;padding:64px 26px 0}
.quote::after{content:"";position:absolute;right:40px;bottom:-14px;border-left:14px solid transparent;border-right:14px solid transparent;border-top:14px solid var(--white)}
.quote .mark{position:absolute;left:24px;top:46px;font-size:28px;font-weight:700;color:var(--ink);line-height:1}
.quote p{font-size:13.5px;line-height:1.55;color:#333;text-align:justify}
.avatar{width:92px;height:92px;border-radius:50%;border:4px solid var(--white);background:radial-gradient(circle at 50% 40%,#c4aa98 0%,#5d544f 60%,#2c2c30 100%)}
.cite{font-size:15px;font-style:italic;font-weight:700;color:var(--navy)}

/* footer */
.site-footer{top:3126px;height:259px;background:var(--navy)}
.foot-brand{top:58px;font-size:54px;color:var(--coral)}
.address{top:134px;font-size:13px;color:var(--white)}
.contacts{top:154px;font-size:12.5px;color:var(--white);display:flex;justify-content:center;gap:16px}
.contacts svg{width:12px;height:12px;vertical-align:-1px;margin-right:4px}
.foot-social{top:190px;left:563px;gap:8px}
.foot-social span{width:22px;height:22px;background:#3aa0e0}
.legal{top:3385px;height:57px;background:var(--bar);color:#eee;font-size:13px;line-height:57px;text-align:center}
</style>
</head>
<body>

<header class="site-header">
  <div class="abs brand">Veltrane</div>
  <nav class="abs main-nav" style="right:196px">
    <span class="active">Home</span><span>Services</span><span>About Us</span><span>Careers</span><span>Contact</span>
  </nav>
  <div class="abs social header-social"><span></span><span></span><span></span></div>
</header>

<section class="hero" role="img" aria-label="Photo of a person touching glowing padlock and fingerprint security rings">
  <div class="abs arrow" style="left:50px;top:270px">&#8249;</div>
  <div class="abs arrow" style="left:1126px;top:270px">&#8250;</div>
  <h1 class="abs center hero-title">Welcome to Veltrane CyberTech (VCT)</h1>
</section>

<section class="about">
  <div class="abs about-art" role="img" aria-label="Illustration of a blue digital padlock with circuit rings"></div>
  <h2 class="abs">About Us</h2>
  <h3 class="abs">Veltrane CyberTech (VCT)</h3>
  <div class="abs rule"></div>
  <p class="abs" style="top:172px">We Provide Advanced Security Engineering and cybersecurity architecture solutions for the commercial sector and federal government.</p>
  <p class="abs" style="top:233px">Our security experts create customized IT solutions for private organizations that meet compliance requirements as well required federal and commercial qualifications</p>
  <p class="abs" style="top:312px">_it's all about YOU, our customer, your needs and your safety.</p>
  <div class="abs btn">Read More</div>
</section>

<section class="services">
  <h2 class="abs center">Services</h2>
  <div class="abs center sub">Veltrane CyberTech (VCT)</div>
  <div class="abs rule"></div>
  <div class="abs arrow" style="left:50px;top:365px">&#8249;</div>
  <div class="abs arrow" style="left:1126px;top:365px">&#8250;</div>

  <div class="abs card" style="left:147px;top:183px"><svg viewBox="0 0 40 40" fill="none" stroke="#1b2a55" stroke-width="1.6"><rect x="12" y="18" width="16" height="13" rx="1"/><path d="M15 18v-4a5 5 0 0 1 10 0v4"/><circle cx="20" cy="24" r="1.5"/></svg><h4>Cyber Security</h4><div class="mini"></div><p>Planning is the key to successfully and legally reducing your tax liability.</p></div>
  <div class="abs card" style="left:381px;top:183px"><svg viewBox="0 0 40 40" fill="none" stroke="#1b2a55" stroke-width="1.6"><rect x="8" y="12" width="24" height="17" rx="1"/><path d="M8 13l12 9 12-9"/></svg><h4>Encrypted Messaging</h4><div class="mini"></div><p>Planning is the key to successfully and legally reducing your tax liability.</p></div>
  <div class="abs card" style="left:617px;top:183px"><svg viewBox="0 0 40 40" fill="none" stroke="#1b2a55" stroke-width="1.6"><rect x="8" y="13" width="24" height="15" rx="2"/><path d="M8 18h24M12 24h6"/></svg><h4>Secure Payment</h4><div class="mini"></div><p>Planning is the key to successfully and legally reducing your tax liability.</p></div>
  <div class="abs card" style="left:853px;top:183px"><svg viewBox="0 0 40 40" fill="none" stroke="#1b2a55" stroke-width="1.6"><rect x="13" y="7" width="14" height="26" rx="2"/><path d="M18 29h4M16 14h8M16 18h8"/></svg><h4>E-mail Virus Thread</h4><div class="mini"></div><p>Planning is the key to successfully and legally reducing your tax liability.</p></div>

  <div class="abs card" style="left:147px;top:413px"><svg viewBox="0 0 40 40" fill="none" stroke="#1b2a55" stroke-width="1.6"><circle cx="20" cy="20" r="10"/><circle cx="20" cy="20" r="6"/><circle cx="20" cy="20" r="2"/></svg><h4>Finger Print Scanner</h4><div class="mini"></div><p>Planning is the key to successfully and legally reducing your tax liability.</p></div>
  <div class="abs card" style="left:381px;top:413px"><svg viewBox="0 0 40 40" fill="none" stroke="#1b2a55" stroke-width="1.6"><path d="M20 7l11 4v9c0 7-5 11-11 13-6-2-11-6-11-13v-9z"/></svg><h4>Global Secure Shield</h4><div class="mini"></div><p>Planning is the key to successfully and legally reducing your tax liability.</p></div>
  <div class="abs card" style="left:617px;top:413px"><svg viewBox="0 0 40 40" fill="none" stroke="#1b2a55" stroke-width="1.6"><rect x="11" y="18" width="18" height="15" rx="2"/><path d="M14 18v-5a6 6 0 0 1 12 0v5"/></svg><h4>Security Padlock</h4><div class="mini"></div><p>Planning is the key to successfully and legally reducing your tax liability.</p></div>
  <div class="abs card" style="left:853px;top:413px"><svg viewBox="0 0 40 40" fill="none" stroke="#1b2a55" stroke-width="1.6"><circle cx="20" cy="20" r="11"/><path d="M16 20l3 3 5-6"/></svg><h4>Mobile Security</h4><div class="mini"></div><p>Planning is the key to successfully and legally reducing your tax liability.</p></div>
</section>

<section class="team">
  <h2 class="abs center">Amazing Team at Veltrane</h2>
  <div class="abs center sub">Meet our Partners</div>
  <div class="abs center sub2">Veltrane CyberTech (VCT)</div>
  <div class="abs rule"></div>
  <div class="abs member" style="left:152px;top:245px"><div class="portrait" role="img" aria-label="Portrait photo of the CEO"></div><h4>Marcus Delaine</h4><div class="role">CEO</div><div class="social"><span></span><span></span><span></span></div></div>
  <div class="abs member" style="left:478px;top:245px"><div class="portrait" role="img" aria-label="Portrait photo of the VP of Business Development"></div><h4>Ivy Castellan</h4><div class="role">VP Business Development</div><div class="social"><span></span><span></span><span></span></div></div>
  <div class="abs member" style="left:802px;top:245px"><div class="portrait" role="img" aria-label="Portrait photo of the CTO"></div><h4>Rafael Ondrey</h4><div class="role">CTO</div><div class="social"><span></span><span></span><span></span></div></div>
</section>

<section class="voices">
  <h2 class="abs center">Awesome People Talk About VCT</h2>
  <div class="abs center sub">Our Customers are Our Heroes!</div>
  <div class="abs rule"></div>
  <div class="abs arrow" style="left:50px;top:335px">&#8249;</div>
  <div class="abs arrow" style="left:1126px;top:335px">&#8250;</div>

  <div class="abs quote" style="left:137px;top:276px"><span class="mark">&ldquo;</span><p>Veltrane - Love coming your way! Best Cybersecurity group we have ever used, Prompt and responsive 7 days a week</p></div>
  <div class="abs avatar" style="left:152px;top:230px" role="img" aria-label="Customer portrait"></div>
  <div class="abs cite" style="left:330px;top:475px">Owen Harcourt</div>

  <div class="abs quote" style="left:465px;top:276px"><span class="mark">&ldquo;</span><p>No one takes care of our cybersecurity against global threats like Rafael &amp; the Veltrane Team</p></div>
  <div class="abs avatar" style="left:480px;top:230px" role="img" aria-label="Customer portrait"></div>
  <div class="abs cite" style="left:627px;top:475px">Leon Whitby</div>

  <div class="abs quote" style="left:789px;top:276px"><span class="mark">&ldquo;</span><p>I can sleep at night, and so can my executive team, thanks to at Veltrane. They are worth their weight in gold!</p></div>
  <div class="abs avatar" style="left:806px;top:230px" role="img" aria-label="Customer portrait"></div>
  <div class="abs cite" style="left:895px;top:475px">Niklas Vestergren</div>
</section>

<footer class="site-footer">
  <div class="abs center foot-brand">Veltrane</div>
  <div class="abs center address">742 W Alder Ln, Maple Ridge, IL 60412</div>
  <div class="abs center contacts">
    <span><svg viewBox="0 0 12 12" fill="#fff"><path d="M2 1h3l1 3-2 1a7 7 0 0 0 3 3l1-2 3 1v3c-6 0-9-4-9-9z"/></svg>555-210-4837</span>
    <span><svg viewBox="0 0 12 12" fill="#fff"><rect x="3" y="0" width="6" height="12" rx="1"/></svg>555-318-9026</span>
    <span><svg viewBox="0 0 12 12" fill="#fff"><rect x="0" y="2" width="12" height="8"/></svg>hello@veltrane.com</span>
    <span><svg viewBox="0 0 12 12" fill="none" stroke="#fff"><circle cx="6" cy="6" r="5"/></svg>www.veltrane.com</span>
  </div>
  <div class="abs social foot-social"><span></span><span></span><span></span></div>
</footer>
<div class="abs legal" style="left:0;width:1200px">&copy; 2017 veltrane.com &nbsp;|&nbsp; Privacy Policy &nbsp;|&nbsp; User Agreement</div>

</body>
</html>
```